Simple, High-Class Web Design Wanted - Motivational Speakers Site

1. Full Brief/Request & Specs outlined on following video -
http://clipvane-recorder.com/watch/tbWrkLmQyP

2. Use colours, images as you feel suits objective (we are happy to pay up to US$30 for any good images but must have licence/permission).

3. Layout probably similar to existing site - www.podiumvoicehub.com.au / http://podiumvoicehub.com.au/contact.php

4. Must Be Able to Coded for MOBILE-FRIENDLINESS & WordPress friendly Ideal.

5. This is the first, small job of many we/graphic design jobs. If suits, winning designer may be offered all future work direct.

Thanks & look forward to your design. Glen.

Target Market(s)

corporates - high end

Number of Pages Required

2 page

Font styles to use
Sans Serif

Requirements
Must have
• Classy professional look
Nice to have
• all in Video in brief
Should not have
• too many images / new images I haven't approved

```html
<!DOCTYPE html>
<html lang="en">
<head>
<meta charset="utf-8">
<title>Free Guest &amp; Conference Speaker Recommendations</title>
<link rel="stylesheet" href="https://fonts.googleapis.com/css2?family=Open+Sans:wght@400;600;700;800&display=swap">
<style>
:root{
  --orange:#f0562a;
  --ink:#1f2328;
  --body:#3a3f45;
  --rule:#d9dbde;
  --band-top:#ffffff;
  --band-mid:#c9cccf;
  --band-bottom:#e9eaec;
  --navy:#15213a;
  --footer:#3b3e42;
  --footer-text:#d6d8da;
}
*{box-sizing:border-box;margin:0;padding:0}
html,body{width:1200px;height:2260px;overflow:hidden;background:#fff}
body{font-family:"Open Sans",Arial,sans-serif;color:var(--body);position:relative}
.page{position:relative;width:1200px;height:2260px}

/* Header */
.masthead{position:absolute;left:0;top:0;width:1200px;height:340px}
.masthead__art{position:absolute;right:22px;top:0;width:300px;height:330px;z-index:1;
  background:linear-gradient(160deg,#f3f3f3 0%,#e6e6e6 45%,#f6c7b4 100%)}
.masthead__title{position:absolute;left:44px;top:18px;z-index:2;color:var(--orange);font-weight:800;line-height:1}
.masthead__title .line1{display:block;font-size:84px;letter-spacing:1px}
.masthead__title .amp{display:block;font-size:58px;margin:0 0 0 200px}
.masthead__title .line2{display:block;font-size:33px;letter-spacing:0;margin-top:6px;white-space:nowrap}
.contact-strip{position:absolute;left:44px;top:252px;z-index:2;display:flex;align-items:center;gap:18px;font-size:20px;color:var(--ink)}
.contact-strip .item{display:flex;align-items:center;gap:10px}
.contact-strip .phone{font-weight:800;font-size:26px;margin-left:150px}

/* Hero band */
.hero{position:absolute;left:0;top:340px;width:1200px;height:750px;
  background:linear-gradient(180deg,var(--band-top) 0%,var(--band-mid) 38%,var(--band-bottom) 100%)}
.hero__heading{position:absolute;left:40px;top:50px;width:1120px;text-align:center;
  font-size:34px;font-weight:700;color:var(--ink);line-height:1.24}
.video-frame{position:absolute;left:258px;top:180px;width:684px;height:400px;border-radius:22px;
  background:#111;padding:18px;box-shadow:0 6px 18px rgba(0,0,0,.35)}
.video-frame__still{width:100%;height:100%;border-radius:6px;
  background:linear-gradient(180deg,#e8ecef 0%,#d7dde2 55%,#8b9fb8 100%)}
.cta-primary{position:absolute;left:262px;top:598px;width:676px;height:64px;background:var(--orange);
  color:#fff;font-size:31px;font-weight:600;text-align:center;line-height:64px;letter-spacing:.3px}

/* Body */
.content{position:absolute;left:64px;top:1100px;width:1072px;font-size:16.5px;line-height:1.5}
.content p{margin-bottom:2px}
.brand{color:var(--orange);font-weight:600}
.criteria{list-style:none;margin:38px 0 0 54px;width:820px}
.criteria li{display:flex;align-items:center;gap:22px;height:66px;border-bottom:1px solid var(--rule);
  font-size:18px;font-weight:700;color:var(--ink);white-space:nowrap}
.criteria li:first-child{border-top:1px solid var(--rule)}
.criteria li svg{flex:none}
.closing{margin-top:28px}

.note{position:absolute;left:64px;top:1702px;width:1072px}
.note__tab{display:inline-block;background:var(--orange);color:#fff;font-weight:700;font-size:20px;padding:6px 22px;
  border-radius:4px 4px 0 0}
.note__list{list-style:none;border-top:2px solid var(--orange);padding-top:18px}
.note__list li{display:flex;gap:16px;font-size:16.5px;line-height:1.5;padding:8px 0 14px;border-bottom:1px solid var(--rule)}
.note__list li svg{flex:none;margin-top:5px}

.cta-secondary{position:absolute;left:410px;top:2024px;width:380px;height:66px;background:var(--navy);border-radius:6px;
  color:#fff;font-size:26px;font-weight:600;text-align:center;line-height:66px}

.site-footer{position:absolute;left:0;top:2130px;width:1200px;height:130px;background:var(--footer);
  color:var(--footer-text);font-size:15px;text-align:center;padding-top:42px;line-height:1.7}
</style>
</head>
<body>
<div class="page">

  <header class="masthead">
    <div class="masthead__art" role="img" aria-label="Illustration of a presenter at a lectern with speech bubbles"></div>
    <h1 class="masthead__title">
      <span class="line1">FREE GUEST</span>
      <span class="amp">&amp;</span>
      <span class="line2">CONFERENCE SPEAKER RECOMMENDATIONS</span>
    </h1>
    <div class="contact-strip">
      <span class="item">
        <svg width="30" height="22" viewBox="0 0 30 22"><rect x="1" y="1" width="28" height="20" rx="2" fill="var(--orange)"/><path d="M2 3l13 10L28 3" fill="none" stroke="#fff" stroke-width="2"/></svg>
        suggestions@podiumvoicehub.com.au
      </span>
      <span class="item phone">
        <svg width="30" height="30" viewBox="0 0 30 30"><rect width="30" height="30" rx="4" fill="var(--orange)"/><path d="M10 7c1 0 2 3 2 4s-2 1-1 3 3 4 4 5 2-1 3-1 4 1 4 2-2 4-4 3-9-4-11-11c-1-3 2-5 3-5z" fill="#fff"/></svg>
        1300 48 27 16
      </span>
    </div>
  </header>

  <section class="hero">
    <h2 class="hero__heading">Are you looking for a Guest or Keynote Speaker - Inspiring,<br>Entertaining, Industry Expert etc, for a conference or special event?</h2>
    <div class="video-frame">
      <div class="video-frame__still" role="img" aria-label="Video still of the presenter speaking to camera"></div>
    </div>
    <div class="cta-primary">I want to Make our Event a Great Success</div>
  </section>

  <main class="content">
    <p><span class="brand">Podium Voice Hub</span> is a free industry service designed to help people looking for speakers save precious time and frustration in finding the most suitable/best speaker for their needs.</p>
    <p>Suggestions are given by Australian conference speaker Glen Harlow, who has presented around Australia for a number of years and is familiar with many of our top professional speakers, MC's as well as the leading speaker bureaus.</p>
    <p>If you would like a hand finding some good speaker options, simply send us the details of your event and the type of presenter you are ideally after, e.g.</p>

    <ul class="criteria">
      <li><svg width="30" height="20" viewBox="0 0 30 20"><path d="M0 7h18V1l12 9-12 9v-6H0z" fill="var(--orange)"/></svg>Type/Style – Motivational, Entertaining, Keynote/Workshop, MC etc</li>
      <li><svg width="30" height="20" viewBox="0 0 30 20"><path d="M0 7h18V1l12 9-12 9v-6H0z" fill="var(--orange)"/></svg>Topic/Area - Team Building, Leadership, Inspiration, Health/Life Balance etc</li>
      <li><svg width="30" height="20" viewBox="0 0 30 20"><path d="M0 7h18V1l12 9-12 9v-6H0z" fill="var(--orange)"/></svg>Approximate Budget - $1000, $2500, $5000, $7500+ etc</li>
      <li><svg width="30" height="20" viewBox="0 0 30 20"><path d="M0 7h18V1l12 9-12 9v-6H0z" fill="var(--orange)"/></svg>Location - Sydney, Melbourne, Brisbane, Perth, Adelaide, Canberra etc</li>
    </ul>

    <p class="closing">and where we can, we will be happy to send you some speaker possibilities/ideas, trusted speakers bureaus or simply some thoughts on the best places for you to look. Regards, Glen.</p>
  </main>

  <section class="note">
    <span class="note__tab">Please Note:</span>
    <ul class="note__list">
      <li><svg width="16" height="16" viewBox="0 0 16 16"><path d="M2 1l13 7-13 7 4-7z" fill="var(--orange)"/></svg>Any information you provide will ONLY ever be used to help with your specific enquiry.</li>
      <li><svg width="16" height="16" viewBox="0 0 16 16"><path d="M2 1l13 7-13 7 4-7z" fill="var(--orange)"/></svg>Glen does not have any financial agreements with any individual speakers he recommends. He offers this service, as it only takes a few minutes of his time, helps promote other professional speakers and obviously keeps his own name out there in the industry.</li>
      <li><svg width="16" height="16" viewBox="0 0 16 16"><path d="M2 1l13 7-13 7 4-7z" fill="var(--orange)"/></svg>Please understand that while Glen tries to respond quickly, due to his own speaking/travel commitments it may take up to 24 hours.</li>
    </ul>
  </section>

  <div class="cta-secondary">Quick Online Contact Form</div>

  <footer class="site-footer">
    © 2015. All Rights Reserved www.podiumvoicehub.com.au PO Box 412 Harbourview NSW 2091<br>
    E-mail: suggestions@podiumvoicehub.com.au Phone: 1300 48 27 16
  </footer>

</div>
</body>
</html>
```